Talvenork Website Concept

We would like a one page website. Please refer to the attached files for more information.

Please reference file attachment version 1.1.

```html
<!DOCTYPE html>
<html lang="en">
<head>
<meta charset="utf-8">
<title>Talvenork Website Concept</title>
<link href="https://fonts.googleapis.com/css2?family=Oswald:wght@600&family=Open+Sans:wght@400;600&family=Arimo:wght@400;700&family=Cinzel:wght@500&display=swap" rel="stylesheet">
<style>
  :root {
    --brand-blue: #1aa0c8;
    --brand-blue-dark: #0e8fb6;
    --header-bg: #f6f6f6;
    --ink: #1a1a1a;
    --nav-ink: #3a3a3a;
    --field-border: #cfcfcf;
    --divider: #9a9a9a;
    --logo-ink: #3d4450;
    --social: #2f7fc0;
    --page-bg: #ffffff;
  }
  * { box-sizing: border-box; margin: 0; padding: 0; }
  html, body { width: 896px; height: 1200px; overflow: hidden; background: var(--page-bg); }
  body { position: relative; font-family: "Arimo", Arial, sans-serif; color: var(--ink); }

  .site-header {
    position: absolute; left: 0; width: 896px; height: 65px;
    background: var(--header-bg);
    border-bottom: 2px solid var(--brand-blue);
  }
  .brand {
    position: absolute; left: 21px; top: 12px; width: 160px; height: 45px;
    background: #fff; display: flex; align-items: center; gap: 8px; padding-left: 4px;
  }
  .brand-mark { width: 26px; height: 26px; background: var(--logo-ink); flex: none; }
  .brand-name {
    font-family: "Cinzel", serif; font-weight: 500; font-size: 22px;
    color: var(--logo-ink); letter-spacing: 0.5px;
  }
  .main-nav {
    position: absolute; top: 0; height: 63px; left: 262px;
    display: flex; align-items: center;
    font-family: "Open Sans", Arial, sans-serif; font-size: 10.5px; font-weight: 600;
  }
  .main-nav a { color: var(--nav-ink); text-decoration: none; padding: 0 17px; }
  .main-nav a.is-current { color: var(--brand-blue); }
  .main-nav .sep { width: 1px; height: 13px; background: var(--divider); }
  .social {
    position: absolute; top: 23px; left: 727px; display: flex; gap: 9px; align-items: center;
  }
  .social span { width: 16px; height: 16px; border-radius: 50%; background: var(--social); display: block; }
  .social .alt { background: #c9302c; border-radius: 3px; }
  .header-rule { position: absolute; left: 824px; top: 21px; width: 1px; height: 22px; background: var(--brand-blue); }
  .search { position: absolute; left: 844px; top: 26px; }

  .section-title {
    position: absolute; left: 0; width: 896px; text-align: center;
    font-family: "Oswald", "Arial Narrow", sans-serif; font-weight: 600; font-size: 23px;
    letter-spacing: 0.3px; color: #111;
  }
  .title-rule { position: absolute; height: 3px; background: var(--brand-blue); }

  .service-strip { position: absolute; left: 21px; top: 180px; width: 854px; height: 145px; display: flex; }
  .service-strip div { flex: 1; }
  .strip-keyboard { background: linear-gradient(135deg, #2a2a2e, #4a1c1c 55%, #1c1c1f); }
  .strip-gears { background: linear-gradient(135deg, #0b1c3a, #1f5a9c 55%, #0c1d36); }
  .strip-network { background: linear-gradient(135deg, #0d1a2c, #3a6a95 50%, #a06a30 75%, #0f1a2a); }
  .strip-headset { background: linear-gradient(135deg, #f2b9c6, #e8a7b8 45%, #3a7fb0 80%, #f1c6d0); }

  .service-list {
    position: absolute; left: 75px; top: 351px; list-style: none;
    font-size: 11.3px; line-height: 16.3px;
  }
  .service-list li { position: relative; padding-left: 17px; }
  .service-list li::before {
    content: ""; position: absolute; left: 0; top: 5px; width: 6px; height: 6px; background: var(--brand-blue);
  }

  .form-intro { position: absolute; left: 78px; top: 661px; font-size: 11px; }
  .field {
    position: absolute; width: 330px; height: 37px;
    border: 1px solid var(--field-border); border-radius: 3px; background: #fff;
    font-size: 11px; padding: 12px 12px; color: #111;
    box-shadow: 0 1px 2px rgba(0,0,0,0.06);
  }
  .field.message { left: 78px; top: 931px; width: 726px; height: 102px; }
  .send-button {
    position: absolute; left: 379px; top: 1045px; width: 130px; height: 37px;
    background: var(--brand-blue); color: #fff; border: none; border-radius: 3px;
    font-family: "Open Sans", Arial, sans-serif; font-weight: 600; font-size: 13px;
  }

  .site-footer {
    position: absolute; left: 0; top: 1168px; width: 896px; height: 32px;
    background: var(--brand-blue); color: #fff; font-size: 11px; font-weight: 700;
  }
  .site-footer .copyright { position: absolute; left: 78px; top: 10px; }
  .site-footer .footer-links { position: absolute; right: 80px; top: 10px; }
</style>
</head>
<body>

  <!-- Header: service offerings page -->
  <header class="site-header" style="top:0;">
    <div class="brand"><span class="brand-mark"></span><span class="brand-name">TALVENORK</span></div>
    <nav class="main-nav">
      <a class="is-current">COMPANY DESCRIPTION</a><span class="sep"></span>
      <a>SERVICE OFFERINGS</a><span class="sep"></span>
      <a>WEBSITE LEAD CAPTURE</a><span class="sep"></span>
    </nav>
    <div class="social" aria-label="Social links"><span></span><span></span><span></span><span class="alt"></span></div>
    <div class="header-rule"></div>
    <svg class="search" width="11" height="11" viewBox="0 0 11 11" aria-label="Search"><circle cx="4.5" cy="4.5" r="3.3" fill="none" stroke="#222" stroke-width="1.6"/><line x1="7" y1="7" x2="10" y2="10" stroke="#222" stroke-width="1.8"/></svg>
  </header>

  <h2 class="section-title" style="top:98px;">SERVICE OFFERINGS</h2>
  <div class="title-rule" style="left:301px; top:136px; width:301px;"></div>

  <div class="service-strip">
    <div class="strip-keyboard" role="img" aria-label="Keyboard with a red service key"></div>
    <div class="strip-gears" role="img" aria-label="Hand touching glowing blue gears"></div>
    <div class="strip-network" role="img" aria-label="Hand touching a digital network of contacts"></div>
    <div class="strip-headset" role="img" aria-label="Support headset with microphone"></div>
  </div>

  <ul class="service-list">
    <li>Threat Assessment</li>
    <li>Threat Avoidance Plan &amp; Dossier Creation</li>
    <li>Elite Executive Protection</li>
    <li>Threat Avoidance Plan &amp; Dossier Maintenance</li>
  </ul>

  <!-- Header: lead capture page -->
  <header class="site-header" style="top:495px;">
    <div class="brand"><span class="brand-mark"></span><span class="brand-name">TALVENORK</span></div>
    <nav class="main-nav">
      <a>COMPANY DESCRIPTION</a><span class="sep"></span>
      <a class="is-current">SERVICE OFFERINGS</a><span class="sep"></span>
      <a>WEBSITE LEAD CAPTURE</a><span class="sep"></span>
    </nav>
    <div class="social" aria-label="Social links"><span></span><span></span><span></span><span class="alt"></span></div>
    <div class="header-rule"></div>
    <svg class="search" width="11" height="11" viewBox="0 0 11 11" aria-label="Search"><circle cx="4.5" cy="4.5" r="3.3" fill="none" stroke="#222" stroke-width="1.6"/><line x1="7" y1="7" x2="10" y2="10" stroke="#222" stroke-width="1.8"/></svg>
  </header>

  <h2 class="section-title" style="top:591px;">WEBSITE LEAD CAPTURE</h2>
  <div class="title-rule" style="left:297px; top:628px; width:300px;"></div>

  <p class="form-intro">Website request for consultation should capture the following information:</p>

  <div class="field" style="left:78px; top:689px;">First Name</div>
  <div class="field" style="left:474px; top:689px;">Last Name</div>
  <div class="field" style="left:78px; top:738px;">Home Phone</div>
  <div class="field" style="left:474px; top:738px;">Work Phone</div>
  <div class="field" style="left:78px; top:786px;">Cell Phone</div>
  <div class="field" style="left:474px; top:786px;">Email Address</div>
  <div class="field" style="left:78px; top:835px;">Address</div>
  <div class="field" style="left:474px; top:835px;">City</div>
  <div class="field" style="left:78px; top:883px;">State</div>
  <div class="field" style="left:474px; top:883px;">Zip</div>
  <div class="field message"></div>
  <button class="send-button">Send Message</button>

  <!-- Header: footer page -->
  <header class="site-header" style="top:1105px; border-bottom:none; height:63px;">
    <div class="brand"><span class="brand-mark"></span><span class="brand-name">TALVENORK</span></div>
    <nav class="main-nav">
      <a>COMPANY DESCRIPTION</a><span class="sep"></span>
      <a>SERVICE OFFERINGS</a><span class="sep"></span>
      <a class="is-current">WEBSITE LEAD CAPTURE</a><span class="sep"></span>
    </nav>
    <div class="social" aria-label="Social links"><span></span><span></span><span></span><span class="alt"></span></div>
    <div class="header-rule"></div>
    <svg class="search" width="11" height="11" viewBox="0 0 11 11" aria-label="Search"><circle cx="4.5" cy="4.5" r="3.3" fill="none" stroke="#222" stroke-width="1.6"/><line x1="7" y1="7" x2="10" y2="10" stroke="#222" stroke-width="1.8"/></svg>
  </header>

  <footer class="site-footer">
    <span class="copyright">Copyright © 2014 Talvenork, LLC. All rights reserved.</span>
    <span class="footer-links">Home | Top</span>
  </footer>

</body>
</html>
```